Pixel Perfect KRX9 style screens

From a high level, we have an existing app that is live in Tunevault. We are in the process of re-branding it to “Palmora” http://palmora-app.example and adding additional features. We have created the wireframe and mockup screens. This project is to create pixel perfect designs of the mock up screens provided, per the details in the word doc. We will accept a portion of the screens, if it includes the main jump screen and at least 4 of the other screens to establish an overall design style/look and feel. I am attaching our new logo. We want to keep the existing brand colors (Blue, Grey, and Orange), with updated logo, possibly making the blue more dominant than the orange (But up to designer), and new photo images. I am attaching one of the images that we are using on the website and in our marketing, but we need to add some additional ones for the new mobile home screen design, website, and marketing. We would like the style and fonts to match the new KRX9 font style guides (Fonts have been changed for KRX9), and everything should adhear to the KRX9 Human Interface guidelines published by quince. Please read the attached design spec doc and mock up screens for additional details.

Target Market(s)

Target Age: 18 - 35, Social Media / Dating

Industry/Entity Type

Social Club

Font styles to use
Other font styles liked:
• New KRX9 font: Marlow Text

Requirements
Must have
• It must conform to the KRX9 human interface guidelines, utilize the latest design elements, and will work on the multiple device sizes Target KRX7 and up, and zPad 5, 5s, 6, and 6plus. The screens must use the company colors, Blue, Orange, and gray:
• Orange: #ff9500
• Blue: #2aa9de
• Light Grey: #e5e5ea
• Medium Grey: #c7c7cc
• Dark Grey: #8e8e93
• White: #ffffff
Nice to have
• UI/UX improvements and recommendations

```html
<!DOCTYPE html>
<html lang="en">
<head>
<meta charset="utf-8">
<title>Palmora — KRX9 screens</title>
<link rel="stylesheet" href="https://fonts.googleapis.com/css2?family=Inter:wght@400;500;600;700&display=swap">
<style>
  :root{
    --orange:#ff9500;
    --blue:#2aa9de;
    --blue-deep:#1b8fc4;
    --grey-light:#e5e5ea;
    --grey-mid:#c7c7cc;
    --grey-dark:#8e8e93;
    --white:#ffffff;
    --ink:#3a3a3c;
    --page:#ffffff;
  }
  *{box-sizing:border-box;margin:0;padding:0}
  html,body{width:1200px;height:2188px;overflow:hidden;background:var(--page)}
  body{font-family:"Inter",Helvetica,Arial,sans-serif;color:var(--ink)}
  .canvas{position:relative;width:1200px;height:2188px;overflow:hidden}

  .screen-title{position:absolute;width:264px;text-align:center;font-size:26px;font-weight:500;color:var(--ink);letter-spacing:-.2px}
  .screen{position:absolute;width:264px;height:472px;border-radius:6px;overflow:hidden;background:var(--white);box-shadow:0 0 0 1px var(--grey-mid);font-size:8px}

  .status-bar{height:10px;background:var(--blue-deep);display:flex;justify-content:space-between;align-items:center;padding:0 6px;color:var(--white);font-size:6px}
  .nav-bar{height:32px;background:var(--blue);display:flex;align-items:center;justify-content:space-between;padding:0 10px;color:var(--white)}
  .brand{font-weight:600;font-size:12px;display:flex;align-items:center;gap:5px}
  .brand-dot{width:9px;height:9px;border-radius:50%;background:var(--white)}
  .nav-icon{width:14px;height:14px}
  .orange-band{height:18px;background:var(--orange);color:var(--white);font-size:8px;display:flex;align-items:center;padding:0 10px;font-weight:600}

  .btn{height:20px;border-radius:4px;display:flex;align-items:center;justify-content:center;color:var(--white);font-weight:600;font-size:8px}
  .btn-blue{background:var(--blue)}
  .btn-orange{background:var(--orange)}
  .photo{background:linear-gradient(135deg,#7d8e9c,#c9b7a3)}
  .avatar{border-radius:50%;background:linear-gradient(135deg,#b79a82,#6f7b86);border:2px solid var(--white)}

  /* Select Nearby */
  .select-body{background:linear-gradient(180deg,#5fc0e8,#2aa9de);height:430px;padding:12px}
  .select-card{background:rgba(255,255,255,.93);border-radius:6px;padding:8px}
  .segment{display:flex;border:1px solid var(--blue);border-radius:4px;overflow:hidden;margin-bottom:8px}
  .segment span{flex:1;text-align:center;padding:3px 0;color:var(--blue);font-weight:600}
  .segment span.on{background:var(--blue);color:var(--white)}
  .section-head{color:var(--blue);font-weight:700;font-size:9px;margin:6px 0 4px}
  .field{height:16px;border:1px solid var(--grey-mid);border-radius:3px;background:var(--white);display:flex;align-items:center;justify-content:space-between;padding:0 6px;color:var(--grey-dark);margin-bottom:4px}
  .field-pair{display:flex;gap:4px}
  .field-pair .field{flex:1}
  .select-actions{display:flex;gap:6px;margin-top:10px}
  .select-actions .btn{flex:1}

  /* Invite Friend */
  .host{display:flex;flex-direction:column;align-items:center;padding:8px 0 2px}
  .host .avatar{width:34px;height:34px;border-color:var(--grey-light)}
  .host-name{font-weight:600;font-size:9px;margin-top:3px}
  .host-sub{color:var(--grey-dark);font-size:7px}
  .orbit{position:relative;height:220px}
  .orbit .featured{position:absolute;left:62px;top:30px;width:140px;height:140px;border-radius:50%;border:4px solid var(--blue)}
  .orbit .small{position:absolute;width:34px;height:34px}
  .featured-name{position:absolute;left:0;right:0;top:178px;text-align:center;font-weight:700;font-size:16px;color:var(--orange)}
  .featured-sub{position:absolute;left:0;right:0;top:198px;text-align:center;color:var(--grey-dark);font-size:7px}
  .tab-row{position:absolute;bottom:0;left:0;right:0;height:44px;border-top:1px solid var(--grey-light);display:flex;justify-content:space-around;align-items:center}
  .tab-row svg{width:20px;height:20px}

  /* Friend Nearby */
  .alert-body{height:462px;background:linear-gradient(180deg,#2aa9de,#1b8fc4);position:relative}
  .alert-card{position:absolute;left:20px;right:20px;top:30px;height:260px;border-radius:6px;overflow:hidden}
  .alert-brand{position:absolute;top:10px;left:0;right:0;text-align:center;color:var(--white);font-weight:700;font-size:14px}
  .alert-text{position:absolute;bottom:16px;left:0;right:0;text-align:center;color:var(--white);font-weight:600;font-size:12px;line-height:1.3}
  .tile-grid{position:absolute;left:20px;right:20px;top:306px;display:grid;grid-template-columns:repeat(3,1fr);gap:6px}
  .tile{height:62px;border-radius:4px;background:rgba(255,255,255,.18);display:flex;align-items:center;justify-content:center}
  .tile svg{width:22px;height:22px}

  /* Request list */
  .list-row{display:flex;align-items:center;gap:7px;padding:6px 8px;border-bottom:1px solid var(--grey-light)}
  .list-row .avatar{width:22px;height:22px;border:none}
  .list-text{flex:1}
  .list-name{font-weight:600;color:var(--blue);font-size:8px}
  .list-sub{color:var(--grey-dark);font-size:6.5px;margin-top:1px}
  .tag{background:var(--orange);color:var(--white);border-radius:3px;padding:2px 5px;font-size:6.5px;font-weight:600}
  .tag.grey{background:var(--grey-mid)}

  /* Details */
  .detail-host{display:flex;flex-direction:column;align-items:center;padding:8px 0}
  .detail-host .avatar{width:40px;height:40px;border-color:var(--grey-light)}
  .when-box{margin:4px 12px;display:flex;align-items:center;gap:12px;border:1px solid var(--grey-light);border-radius:5px;padding:8px}
  .cal{width:44px;height:48px;border-radius:4px;overflow:hidden;border:1px solid var(--grey-mid);text-align:center}
  .cal-top{background:var(--orange);color:var(--white);font-size:7px;padding:2px 0}
  .cal-day{font-size:22px;font-weight:600;color:var(--ink)}
  .when-month{font-size:18px;font-weight:300;color:var(--grey-dark)}
  .when-time{font-size:8px;color:var(--orange);margin-top:2px}
  .where-photo{margin:4px 12px;height:96px;border-radius:5px;position:relative;overflow:hidden}
  .where-label{position:absolute;left:8px;bottom:6px;color:var(--white);font-weight:600;font-size:9px}
  .comments-head{margin:10px 12px 4px;color:var(--blue);font-weight:700;font-size:8px}
  .comment{display:flex;gap:6px;align-items:center;margin:0 12px 6px;padding-bottom:5px;border-bottom:1px solid var(--grey-light)}
  .comment .avatar{width:16px;height:16px;border:none}
  .comment-line{flex:1;color:var(--grey-dark);font-size:7px}
  .reply{margin:8px 12px;height:18px;border:1px solid var(--grey-mid);border-radius:9px;color:var(--grey-mid);font-size:7px;display:flex;align-items:center;padding:0 8px}
  .detail-cta{margin:8px 60px 0}

  /* Joined list */
  .joined-row{display:flex;justify-content:center;gap:8px;margin:6px 0 10px}
  .joined-row .avatar{width:34px;height:34px;border-color:var(--blue)}
  .joined-label{text-align:center;font-weight:700;color:var(--blue);font-size:8px}

  /* Hotspot */
  .hotspot{height:472px;position:relative}
  .hotspot-photo{position:absolute;inset:0;background:linear-gradient(180deg,#1e9fd6 0%,#6a4c8c 45%,#e4763a 75%,#2a1f2e 100%)}
  .hotspot-brand{position:absolute;top:60px;left:0;right:0;text-align:center;color:var(--white);font-weight:700;font-size:18px;display:flex;align-items:center;justify-content:center;gap:7px}
  .hotspot-brand .brand-dot{width:14px;height:14px}
  .hotspot-text{position:absolute;top:330px;left:0;right:0;text-align:center;color:var(--white);font-weight:600;font-size:11px}
  .hotspot-tiles{position:absolute;left:10px;right:10px;bottom:14px;display:grid;grid-template-columns:repeat(4,1fr);gap:5px}
  .hotspot-tiles .tile{height:50px;background:rgba(255,255,255,.22)}

  /* Event list */
  .search{margin:6px 8px;height:16px;background:var(--grey-light);border-radius:8px;color:var(--grey-dark);font-size:7px;display:flex;align-items:center;padding:0 8px;gap:4px}
  .list-section{background:var(--blue);color:var(--white);font-weight:600;font-size:7px;padding:3px 8px}
  .event-row{display:flex;align-items:center;gap:7px;padding:5px 8px;border-bottom:1px solid var(--grey-light)}
  .event-thumb{width:22px;height:22px;border-radius:3px}
  .go{width:14px;height:14px;border-radius:50%;background:var(--blue);display:flex;align-items:center;justify-content:center}
  .go svg{width:8px;height:8px}
  .tab-footer{position:absolute;left:0;right:0;bottom:0;height:28px;border-top:1px solid var(--grey-light);display:flex;justify-content:space-around;align-items:center;background:var(--white)}
  .tab-footer span{color:var(--grey-dark);font-size:7px}
  .tab-footer span.on{color:var(--blue);font-weight:600}
</style>
</head>
<body>
<main class="canvas">

  <!-- Row 1 titles -->
  <h2 class="screen-title" style="left:88px;top:98px">Select Nearby</h2>
  <h2 class="screen-title" style="left:468px;top:98px">Invite Friend</h2>
  <h2 class="screen-title" style="left:848px;top:98px">Friend Nearby</h2>

  <!-- Select Nearby -->
  <section class="screen" style="left:88px;top:160px">
    <div class="status-bar"><span>●●●●● Carrier</span><span>9:41</span><span>100%</span></div>
    <header class="nav-bar">
      <svg class="nav-icon" viewBox="0 0 14 14"><path d="M2 3h10M2 7h10M2 11h10" stroke="#fff" stroke-width="1.6"/></svg>
      <span class="brand"><span class="brand-dot"></span>Palmora</span>
      <span style="width:14px"></span>
    </header>
    <div class="select-body">
      <div class="select-card">
        <div class="segment"><span class="on">Nearby</span><span>Invite</span></div>
        <p class="section-head">Select A Place or Activity</p>
        <div class="field"><span>Choose a place</span><span>›</span></div>
        <div class="field"><span>Enter a location</span><span>›</span></div>
        <div class="field"><span>Or pick an activity</span><span>›</span></div>
        <p class="section-head">Select a Date and Time</p>
        <div class="field-pair">
          <div class="field"><span>Date</span><span>›</span></div>
          <div class="field"><span>Time</span><span>›</span></div>
        </div>
        <div class="field"><span>Anytime</span><span>›</span></div>
        <div class="select-actions">
          <span class="btn btn-blue">Cancel</span>
          <span class="btn btn-orange">Done</span>
        </div>
      </div>
    </div>
  </section>

  <!-- Invite Friend -->
  <section class="screen" style="left:468px;top:160px">
    <div class="status-bar"><span>●●●●● Carrier</span><span>9:41</span><span>100%</span></div>
    <header class="nav-bar">
      <svg class="nav-icon" viewBox="0 0 14 14"><path d="M2 3h10M2 7h10M2 11h10" stroke="#fff" stroke-width="1.6"/></svg>
      <span class="brand"><span class="brand-dot"></span>Palmora</span>
      <svg class="nav-icon" viewBox="0 0 14 14"><circle cx="6" cy="6" r="4" fill="none" stroke="#fff" stroke-width="1.5"/><path d="M9 9l3 3" stroke="#fff" stroke-width="1.5"/></svg>
    </header>
    <div class="orange-band">Who are you Palmora with?</div>
    <div class="host">
      <div class="avatar" role="img" aria-label="Profile photo of the host"></div>
      <div class="host-name">Dale Corwin</div>
      <div class="host-sub">2 miles away</div>
    </div>
    <div class="orbit">
      <div class="avatar small" style="left:16px;top:10px" role="img" aria-label="Friend photo"></div>
      <div class="avatar small" style="left:214px;top:10px" role="img" aria-label="Friend photo"></div>
      <div class="avatar small" style="left:8px;top:120px" role="img" aria-label="Friend photo"></div>
      <div class="avatar small" style="left:222px;top:120px" role="img" aria-label="Friend photo"></div>
      <div class="featured photo" role="img" aria-label="Large portrait photo of the selected friend"></div>
      <div class="featured-name">Mirela</div>
      <div class="featured-sub">Tap to invite</div>
    </div>
    <nav class="tab-row">
      <svg viewBox="0 0 20 20"><circle cx="10" cy="10" r="8" fill="none" stroke="#8e8e93" stroke-width="1.5"/><path d="M10 5v5l3 2" stroke="#8e8e93" stroke-width="1.5" fill="none"/></svg>
      <svg viewBox="0 0 20 20"><circle cx="10" cy="10" r="9" fill="#ff9500"/><path d="M6 10h8M10 6v8" stroke="#fff" stroke-width="2"/></svg>
      <svg viewBox="0 0 20 20"><circle cx="10" cy="10" r="8" fill="none" stroke="#2aa9de" stroke-width="1.5"/><path d="M6 10l3 3 5-6" stroke="#2aa9de" stroke-width="1.8" fill="none"/></svg>
    </nav>
  </section>

  <!-- Friend Nearby -->
  <section class="screen" style="left:848px;top:160px">
    <div class="status-bar"><span>●●●●● Carrier</span><span>9:41</span><span>100%</span></div>
    <div class="alert-body">
      <div class="alert-card photo" role="img" aria-label="Photo of friends meeting and smiling together">
        <div class="alert-brand">Palmora</div>
        <div class="alert-text">Palmora<br>Request Nearby</div>
      </div>
      <div class="tile-grid">
        <div class="tile"><svg viewBox="0 0 22 22"><path d="M11 2a6 6 0 0 1 6 6c0 5-6 12-6 12S5 13 5 8a6 6 0 0 1 6-6z" fill="none" stroke="#fff" stroke-width="1.6"/><circle cx="11" cy="8" r="2" fill="#fff"/></svg></div>
        <div class="tile"><svg viewBox="0 0 22 22"><circle cx="11" cy="8" r="4" fill="none" stroke="#fff" stroke-width="1.6"/><path d="M3 20c1-5 15-5 16 0" fill="none" stroke="#fff" stroke-width="1.6"/></svg></div>
        <div class="tile"><svg viewBox="0 0 22 22"><rect x="3" y="5" width="16" height="14" rx="2" fill="none" stroke="#fff" stroke-width="1.6"/><path d="M3 9h16M7 3v4M15 3v4" stroke="#fff" stroke-width="1.6"/></svg></div>
        <div class="tile"><svg viewBox="0 0 22 22"><path d="M4 5h14v10H9l-4 3v-3H4z" fill="none" stroke="#fff" stroke-width="1.6"/></svg></div>
        <div class="tile"><svg viewBox="0 0 22 22"><path d="M5 11l4 4 8-9" fill="none" stroke="#fff" stroke-width="2"/></svg></div>
        <div class="tile"><svg viewBox="0 0 22 22"><path d="M6 6l10 10M16 6L6 16" stroke="#fff" stroke-width="2"/></svg></div>
      </div>
    </div>
  </section>

  <!-- Row 2 titles -->
  <h2 class="screen-title" style="left:68px;top:798px;width:304px">List of Friend Request</h2>
  <h2 class="screen-title" style="left:448px;top:798px;width:304px">Details of Invite “WHEN”</h2>
  <h2 class="screen-title" style="left:828px;top:798px;width:304px">Details of Invite “WHERE”</h2>

  <!-- Friend Request list -->
  <section class="screen" style="left:88px;top:860px">
    <div class="status-bar"><span>●●●●● Carrier</span><span>9:41</span><span>100%</span></div>
    <header class="nav-bar">
      <svg class="nav-icon" viewBox="0 0 14 14"><path d="M2 3h10M2 7h10M2 11h10" stroke="#fff" stroke-width="1.6"/></svg>
      <span class="brand"><span class="brand-dot"></span>Palmora</span>
      <span style="width:14px"></span>
    </header>
    <div class="orange-band">Friend Requests</div>
    <div class="list-row"><div class="avatar" role="img" aria-label="Friend photo"></div><div class="list-text"><div class="list-name">Nora Vale</div><div class="list-sub">Coffee · 2 min ago</div></div><span class="tag">New</span></div>
    <div class="list-row"><div class="avatar" role="img" aria-label="Friend photo"></div><div class="list-text"><div class="list-name">Owen Pratt</div><div class="list-sub">Lunch · 8 min ago</div></div><span class="tag">New</span></div>
    <div class="list-row"><div class="avatar" role="img" aria-label="Friend photo"></div><div class="list-text"><div class="list-name">Lia Moreno</div><div class="list-sub">Movies · 15 min ago</div></div><span class="tag grey">Seen</span></div>
    <div class="list-row"><div class="avatar" role="img" aria-label="Friend photo"></div><div class="list-text"><div class="list-name">Theo Marsh</div><div class="list-sub">Drinks · 1 hr ago</div></div><span class="tag grey">Seen</span></div>
    <div class="list-row"><div class="avatar" role="img" aria-label="Friend photo"></div><div class="list-text"><div class="list-name">Ada Quinn</div><div class="list-sub">Hiking · 2 hr ago</div></div><span class="tag">New</span></div>
    <div class="list-row"><div class="avatar" role="img" aria-label="Friend photo"></div><div class="list-text"><div class="list-name">Milo Reyes</div><div class="list-sub">Gym · 3 hr ago</div></div><span class="tag grey">Seen</span></div>
    <div class="list-row"><div class="avatar" role="img" aria-label="Friend photo"></div><div class="list-text"><div class="list-name">Ivy Lark</div><div class="list-sub">Brunch · 5 hr ago</div></div><span class="tag grey">Seen</span></div>
    <div class="list-row"><div class="avatar" role="img" aria-label="Friend photo"></div><div class="list-text"><div class="list-name">Remy Stone</div><div class="list-sub">Concert · 1 day ago</div></div><span class="tag grey">Seen</span></div>
    <div class="list-row"><div class="avatar" role="img" aria-label="Friend photo"></div><div class="list-text"><div class="list-name">June Hale</div><div class="list-sub">Dinner · 2 days ago</div></div><span class="tag grey">Seen</span></div>
    <div class="list-row"><div class="avatar" role="img" aria-label="Friend photo"></div><div class="list-text"><div class="list-name">Cole Baird</div><div class="list-sub">Beach · 3 days ago</div></div><span class="tag grey">Seen</span></div>
  </section>

  <!-- Details WHEN -->
  <section class="screen" style="left:468px;top:860px">
    <div class="status-bar"><span>●●●●● Carrier</span><span>9:41</span><span>100%</span></div>
    <header class="nav-bar">
      <svg class="nav-icon" viewBox="0 0 14 14"><path d="M9 2L4 7l5 5" stroke="#fff" stroke-width="1.6" fill="none"/></svg>
      <span class="brand"><span class="brand-dot"></span>Palmora</span>
      <span style="width:14px"></span>
    </header>
    <div class="orange-band">When</div>
    <div class="detail-host">
      <div class="avatar" role="img" aria-label="Profile photo of the host"></div>
      <div class="host-name">Dale Corwin</div>
      <div class="host-sub">invited you</div>
    </div>
    <div class="when-box">
      <div class="cal"><div class="cal-top">MON</div><div class="cal-day">3</div></div>
      <div><div class="when-month">August 2015</div><div class="when-time">● 7:00 pm</div></div>
    </div>
    <p class="comments-head">COMMENTS</p>
    <div class="comment"><div class="avatar" role="img" aria-label="Commenter photo"></div><span class="comment-line">Sounds great, see you!</span></div>
    <div class="comment"><div class="avatar" role="img" aria-label="Commenter photo"></div><span class="comment-line">Can we start a bit later?</span></div>
    <div class="reply">Write a comment…</div>
    <div class="detail-cta"><span class="btn btn-blue">Join</span></div>
  </section>

  <!-- Details WHERE -->
  <section class="screen" style="left:848px;top:860px">
    <div class="status-bar"><span>●●●●● Carrier</span><span>9:41</span><span>100%</span></div>
    <header class="nav-bar">
      <svg class="nav-icon" viewBox="0 0 14 14"><path d="M9 2L4 7l5 5" stroke="#fff" stroke-width="1.6" fill="none"/></svg>
      <span class="brand"><span class="brand-dot"></span>Palmora</span>
      <span style="width:14px"></span>
    </header>
    <div class="orange-band">Where</div>
    <div class="detail-host">
      <div class="avatar" role="img" aria-label="Profile photo of the host"></div>
      <div class="host-name">Dale Corwin</div>
      <div class="host-sub">invited you</div>
    </div>
    <div class="where-photo photo" role="img" aria-label="Photo of the meeting venue">
      <span class="where-label">Harbor Street Café</span>
    </div>
    <p class="comments-head">COMMENTS</p>
    <div class="comment"><div class="avatar" role="img" aria-label="Commenter photo"></div><span class="comment-line">Love this place!</span></div>
    <div class="reply">Write a comment…</div>
    <div class="detail-cta"><span class="btn btn-blue">Join</span></div>
  </section>

  <!-- Row 3 titles -->
  <h2 class="screen-title" style="left:68px;top:1518px;width:304px">JOINED LIST “WHO”</h2>
  <h2 class="screen-title" style="left:468px;top:1518px">Hotspot &amp; Events</h2>
  <h2 class="screen-title" style="left:848px;top:1518px">Event Nearby</h2>

  <!-- Joined list -->
  <section class="screen" style="left:88px;top:1580px">
    <div class="status-bar"><span>●●●●● Carrier</span><span>9:41</span><span>100%</span></div>
    <header class="nav-bar">
      <svg class="nav-icon" viewBox="0 0 14 14"><path d="M9 2L4 7l5 5" stroke="#fff" stroke-width="1.6" fill="none"/></svg>
      <span class="brand"><span class="brand-dot"></span>Palmora</span>
      <span style="width:14px"></span>
    </header>
    <div class="orange-band">Who</div>
    <div class="detail-host">
      <div class="avatar" role="img" aria-label="Profile photo of the host"></div>
      <div class="host-name">Dale Corwin</div>
      <div class="host-sub">host</div>
    </div>
    <p class="joined-label">JOINED</p>
    <div class="joined-row">
      <div class="avatar" role="img" aria-label="Guest photo"></div>
      <div class="avatar" role="img" aria-label="Guest photo"></div>
      <div class="avatar" role="img" aria-label="Guest photo"></div>
      <div class="avatar" role="img" aria-label="Guest photo"></div>
    </div>
    <p class="comments-head">COMMENTS</p>
    <div class="comment"><div class="avatar" role="img" aria-label="Commenter photo"></div><span class="comment-line">I'm in, bringing a friend.</span></div>
    <div class="comment"><div class="avatar" role="img" aria-label="Commenter photo"></div><span class="comment-line">Count me in too!</span></div>
    <div class="reply">Write a comment…</div>
    <div class="detail-cta"><span class="btn btn-blue">Join</span></div>
  </section>

  <!-- Hotspot & Events -->
  <section class="screen" style="left:468px;top:1580px">
    <div class="hotspot">
      <div class="hotspot-photo" role="img" aria-label="Photo of a crowd at a concert under stage lights"></div>
      <div class="hotspot-brand"><span class="brand-dot"></span>Palmora</div>
      <div class="hotspot-text">Hotspots &amp; Events Near You</div>
      <div class="hotspot-tiles">
        <div class="tile"><svg viewBox="0 0 22 22"><path d="M11 2a6 6 0 0 1 6 6c0 5-6 12-6 12S5 13 5 8a6 6 0 0 1 6-6z" fill="none" stroke="#fff" stroke-width="1.6"/></svg></div>
        <div class="tile"><svg viewBox="0 0 22 22"><path d="M8 16V5l10-2v11" fill="none" stroke="#fff" stroke-width="1.6"/><circle cx="6" cy="16" r="2.5" fill="#fff"/><circle cx="16" cy="14" r="2.5" fill="#fff"/></svg></div>
        <div class="tile"><svg viewBox="0 0 22 22"><rect x="3" y="5" width="16" height="14" rx="2" fill="none" stroke="#fff" stroke-width="1.6"/><path d="M3 9h16" stroke="#fff" stroke-width="1.6"/></svg></div>
        <div class="tile"><svg viewBox="0 0 22 22"><circle cx="11" cy="8" r="4" fill="none" stroke="#fff" stroke-width="1.6"/><path d="M3 20c1-5 15-5 16 0" fill="none" stroke="#fff" stroke-width="1.6"/></svg></div>
      </div>
    </div>
  </section>

  <!-- Event Nearby -->
  <section class="screen" style="left:848px;top:1580px">
    <div class="status-bar"><span>●●●●● Carrier</span><span>9:41</span><span>100%</span></div>
    <header class="nav-bar">
      <svg class="nav-icon" viewBox="0 0 14 14"><path d="M2 3h10M2 7h10M2 11h10" stroke="#fff" stroke-width="1.6"/></svg>
      <span class="brand"><span class="brand-dot"></span>Palmora</span>
      <span style="width:14px"></span>
    </header>
    <div class="search"><svg width="8" height="8" viewBox="0 0 14 14"><circle cx="6" cy="6" r="4" fill="none" stroke="#8e8e93" stroke-width="1.6"/><path d="M9 9l3 3" stroke="#8e8e93" stroke-width="1.6"/></svg>Search events</div>
    <div class="list-section">TONIGHT</div>
    <div class="event-row"><div class="event-thumb photo" role="img" aria-label="Event photo"></div><div class="list-text"><div class="list-name">Rooftop Live Set</div><div class="list-sub">0.4 mi · 9:00 pm</div></div><span class="go"><svg viewBox="0 0 8 8"><path d="M3 1l3 3-3 3" stroke="#fff" stroke-width="1.3" fill="none"/></svg></span></div>
    <div class="event-row"><div class="event-thumb photo" role="img" aria-label="Event photo"></div><div class="list-text"><div class="list-name">Jazz at Pier 9</div><div class="list-sub">0.8 mi · 8:30 pm</div></div><span class="go"><svg viewBox="0 0 8 8"><path d="M3 1l3 3-3 3" stroke="#fff" stroke-width="1.3" fill="none"/></svg></span></div>
    <div class="event-row"><div class="event-thumb photo" role="img" aria-label="Event photo"></div><div class="list-text"><div class="list-name">Trivia Night</div><div class="list-sub">1.1 mi · 7:00 pm</div></div><span class="go"><svg viewBox="0 0 8 8"><path d="M3 1l3 3-3 3" stroke="#fff" stroke-width="1.3" fill="none"/></svg></span></div>
    <div class="event-row"><div class="event-thumb photo" role="img" aria-label="Event photo"></div><div class="list-text"><div class="list-name">Salsa Social</div><div class="list-sub">1.5 mi · 10:00 pm</div></div><span class="go"><svg viewBox="0 0 8 8"><path d="M3 1l3 3-3 3" stroke="#fff" stroke-width="1.3" fill="none"/></svg></span></div>
    <div class="list-section">THIS WEEKEND</div>
    <div class="event-row"><div class="event-thumb photo" role="img" aria-label="Event photo"></div><div class="list-text"><div class="list-name">Street Food Fair</div><div class="list-sub">2.0 mi · Sat noon</div></div><span class="go"><svg viewBox="0 0 8 8"><path d="M3 1l3 3-3 3" stroke="#fff" stroke-width="1.3" fill="none"/></svg></span></div>
    <div class="event-row"><div class="event-thumb photo" role="img" aria-label="Event photo"></div><div class="list-text"><div class="list-name">Beach Volleyball</div><div class="list-sub">3.2 mi · Sat 3 pm</div></div><span class="go"><svg viewBox="0 0 8 8"><path d="M3 1l3 3-3 3" stroke="#fff" stroke-width="1.3" fill="none"/></svg></span></div>
    <div class="event-row"><div class="event-thumb photo" role="img" aria-label="Event photo"></div><div class="list-text"><div class="list-name">Open Air Cinema</div><div class="list-sub">2.6 mi · Sun 8 pm</div></div><span class="go"><svg viewBox="0 0 8 8"><path d="M3 1l3 3-3 3" stroke="#fff" stroke-width="1.3" fill="none"/></svg></span></div>
    <nav class="tab-footer"><span class="on">Nearby</span><span>Events</span><span>Friends</span></nav>
  </section>

</main>
</body>
</html>
```